Lodge By The Riverbend Business Card

Here's our website: www.lodgebytheriverbendelmridge.example I need a business card that reflects the business. I'd like some kind of mountain or cabin or cabin on a mountain type motif on there. Maybe the card is shaped like a cabin - not sure.
The card will have the address on there, my name, our phone number, email,website address and 'Find us on STYX/Dwellnest/ Kipzo and Journeyscout. Front and back design requested.

Target Market(s)

Vacationers looking for the ultimate mountain getaway near a fun ski town/ summer resort.

Industry/Entity Type

Business

Font styles to use
Serif

Colors
f37022
f79020

Requirements
Must have
• Business card sized. Not larger or smaller
Nice to have
• I want the cabin and or mountain theme incorporated
Should not have
• Nothing contemporary looking

```html
<!DOCTYPE html>
<html lang="en">
<head>
<meta charset="utf-8">
<title>Lodge By The Riverbend – Business Card</title>
<link href="https://fonts.googleapis.com/css2?family=Questrial&display=swap" rel="stylesheet">
<style>
  :root {
    --backdrop: #4a2c1d;
    --orange: #f37022;
    --orange-light: #f88a3a;
    --orange-deep: #ec6a1c;
    --cream: #f6e2cc;
    --cream-line: #e9cdb0;
    --ink: #231f1c;
    --photo-sky: #7f8a8e;
    --photo-glow: #f79020;
    --photo-snow: #d9d9dc;
    --photo-dark: #3a2a24;
  }
  * { margin: 0; padding: 0; box-sizing: border-box; }
  html, body {
    width: 1200px; height: 1000px; overflow: hidden;
    background: var(--backdrop);
    font-family: "Questrial", "Century Gothic", sans-serif;
  }
  .canvas { position: relative; width: 1200px; height: 1000px; }

  .card {
    position: absolute; left: 174px; width: 742px; height: 445px;
    background: linear-gradient(160deg, var(--orange-light) 0%, var(--orange) 55%, var(--orange-deep) 100%);
    overflow: hidden;
  }
  .card--front { top: 41px; }
  .card--back { top: 524px; }

  .ribbon {
    position: absolute; top: 0; height: 100%;
    background: var(--cream);
    border-left: 11px solid var(--ink);
    border-right: 10px solid var(--ink);
  }
  .card--front .ribbon { left: 411px; width: 180px; }
  .card--back .ribbon { left: 99px; width: 180px; }

  .photo {
    position: absolute; left: 48px; top: 48px; width: 645px; height: 348px;
    border: 2px solid var(--orange-deep);
    background: linear-gradient(180deg,
      var(--photo-sky) 0%, var(--photo-sky) 14%,
      var(--photo-glow) 22%, #c76a45 36%,
      var(--photo-snow) 55%, var(--photo-dark) 72%,
      var(--photo-snow) 92%, #eeeeee 100%);
  }

  .label {
    position: absolute; left: 91px; top: 154px; width: 194px; height: 126px;
    background: var(--cream);
    display: flex; flex-direction: column; align-items: center; justify-content: center;
  }
  .label__rule {
    position: absolute; left: 7px; right: 7px; height: 14px;
    border-top: 3px solid var(--ink); border-bottom: 3px solid var(--ink);
  }
  .label__rule::after {
    content: ""; position: absolute; left: 0; right: 0; top: 3px; height: 2px; background: var(--ink);
  }
  .label__rule--top { top: 7px; }
  .label__rule--bottom { bottom: 6px; }
  .label__name {
    font-size: 21px; color: var(--ink); letter-spacing: 0.2px; margin-top: -6px;
  }
  .label__flourish { margin-top: 6px; }

  .contact { position: absolute; color: var(--ink); }
  .contact__web { left: 313px; top: 137px; font-size: 17.5px; }
  .contact__line { left: 315px; font-size: 15px; }
  .contact__line--name { top: 182px; }
  .contact__line--phone { top: 224px; }
  .contact__line--email { top: 266px; }
  .contact__line--site { top: 308px; }
  .contact__listings { left: 293px; top: 365px; font-size: 16px; }
</style>
</head>
<body>
<main class="canvas">
  <section class="card card--front" aria-label="Card front">
    <div class="ribbon"></div>
    <div class="photo" role="img" aria-label="Photograph of a log lodge in the snow with sunset-lit mountains behind"></div>
  </section>

  <section class="card card--back" aria-label="Card back">
    <div class="ribbon"></div>
    <div class="label">
      <span class="label__rule label__rule--top"></span>
      <span class="label__name">COMPANY NAME</span>
      <svg class="label__flourish" width="80" height="8" viewBox="0 0 80 8" aria-hidden="true">
        <line x1="2" y1="4" x2="78" y2="4" stroke="#231f1c" stroke-width="1"/>
      </svg>
      <span class="label__rule label__rule--bottom"></span>
    </div>
    <p class="contact contact__web">www.lodgebytheriverbendelmridge.example</p>
    <p class="contact contact__line contact__line--name">name</p>
    <p class="contact contact__line contact__line--phone">phone number</p>
    <p class="contact contact__line contact__line--email">email</p>
    <p class="contact contact__line contact__line--site">website address</p>
    <p class="contact contact__listings">Find us on STYX/Dwellnest/ Kipzo and Journeyscout</p>
  </section>
</main>
</body>
</html>
```